Harborlight Capital Estates business card

We are a real estate advisory and investment company. We are specialized in assisting high networth individuals to invest in real estate overseas. We deliver a very personalized service, anticipating all the potential challenges an investor can face, and making it easy and safe for them. We also co-invest with our clients, assuring them that each project will be looked after as it is our own, and at the same time giving them the extra booth on confidence to invest.

We need a business card design. The business card must have a very premium, high-end look, reflecting principles like "commitment", "trust" and "timeless (but contemporary)". We look for long term relationships with our clients, and we grow with their referrals. We are all about conquering the confidence of the clients by always delivering above the expectations performance.

Target Market(s)

High net worth individuals.

Industry/Entity Type

Real Estate

Contact Information for Business Card

Please consider places on the business card for:

Name
Function (bellow name in smaller size text)

Mobile phone
E-mail
Skype ID
WeChat ID

Adress (3 lines)

Also include the following locations references:
PORTUGAL * DUBAI * HONG KONG

Website: www.hcestates-example.com

Requirements
Must have
• Company Logo

```html
<!DOCTYPE html>
<html lang="en">
<head>
<meta charset="utf-8">
<title>Harborlight Capital Estates business card</title>
<link rel="stylesheet" href="https://fonts.googleapis.com/css2?family=Montserrat:wght@400;500;600&display=swap">
<style>
  :root {
    --stage: #ecebe8;
    --brand-blue: #29a8e0;
    --band-grey: #8c8d90;
    --ink-grey: #5d5f63;
    --rule-grey: #9a9ca0;
    --card-white: #ffffff;
    --chat-green: #3fb54a;
  }
  * { box-sizing: border-box; margin: 0; padding: 0; }
  html, body {
    width: 1200px; height: 900px; overflow: hidden;
    background: var(--stage);
    font-family: "Montserrat", sans-serif;
  }
  .stage {
    position: relative; width: 1200px; height: 900px;
    display: flex; flex-direction: column; align-items: center; justify-content: center; gap: 40px;
  }
  .card {
    position: relative; width: 640px; height: 366px;
    border-radius: 24px; overflow: hidden;
    box-shadow: 0 6px 18px rgba(0,0,0,0.12);
  }

  /* back side */
  .card-back { background: var(--brand-blue); color: var(--card-white); }
  .card-back .brand-name {
    position: absolute; left: 0; right: 0; top: 92px;
    text-align: center; font-size: 30px; font-weight: 500;
    letter-spacing: 3px; line-height: 1.25; text-transform: uppercase;
    color: var(--card-white);
  }
  .location-band {
    position: absolute; left: 0; right: 0; top: 222px; height: 34px;
    background: var(--band-grey);
    display: flex; align-items: center; justify-content: flex-end; padding-right: 44px;
    font-size: 15px; letter-spacing: 1px; color: var(--card-white);
  }
  .location-band .dot {
    display: inline-block; width: 7px; height: 7px; border-radius: 50%;
    background: var(--card-white); margin: 0 14px; vertical-align: middle;
  }
  .card-back .website {
    position: absolute; right: 44px; top: 276px; font-size: 17px; color: var(--card-white);
  }

  /* front side */
  .card-front { background: var(--card-white); }
  .holder { position: absolute; left: 48px; top: 36px; }
  .holder .name { font-size: 23px; font-weight: 500; color: var(--brand-blue); }
  .holder .position { font-size: 14px; color: var(--ink-grey); margin-top: 2px; }
  .card-front .brand-name {
    position: absolute; right: 44px; top: 96px; text-align: right;
    font-size: 22px; font-weight: 500; letter-spacing: 2px; line-height: 1.3;
    text-transform: uppercase; color: var(--brand-blue);
  }
  .divider { position: absolute; left: 0; top: 196px; width: 640px; height: 20px; }
  .contacts { position: absolute; left: 48px; top: 228px; list-style: none; }
  .contacts li {
    display: flex; align-items: center; gap: 12px;
    font-size: 15px; color: var(--ink-grey); height: 24px;
  }
  .contacts .icon { width: 14px; height: 14px; flex: none; }
  .contacts .web-accent { color: var(--brand-blue); }
  .address {
    position: absolute; right: 44px; bottom: 34px;
    display: flex; gap: 8px; font-size: 15px; line-height: 1.3; color: var(--ink-grey);
  }
  .address .icon { width: 12px; height: 16px; flex: none; margin-top: 2px; }
</style>
</head>
<body>
<main class="stage">

  <section class="card card-back" aria-label="Card back">
    <div class="brand-name">Harborlight<br>Capital Estates</div>
    <div class="location-band">PORTUGAL<span class="dot"></span>DUBAI<span class="dot"></span>HONG KONG</div>
    <div class="website">www.hcestates-example.com</div>
  </section>

  <section class="card card-front" aria-label="Card front">
    <div class="holder">
      <div class="name">Your Name</div>
      <div class="position">position</div>
    </div>
    <div class="brand-name">Harborlight<br>Capital Estates</div>

    <svg class="divider" viewBox="0 0 640 20" aria-hidden="true">
      <path d="M0 12 H92 L102 3 L112 12 H640" fill="none" stroke="var(--rule-grey)" stroke-width="1.2"/>
    </svg>

    <ul class="contacts">
      <li>
        <svg class="icon" viewBox="0 0 14 14" aria-hidden="true"><path d="M3 1 L5 1 L6 4 L4.5 5.5 Q6 8.5 8.5 9.5 L10 8 L13 9 L13 11 Q12 13 10 13 Q3 11 1 4 Q1 2 3 1Z" fill="var(--ink-grey)"/></svg>
        +91 7350 482210
      </li>
      <li>
        <svg class="icon" viewBox="0 0 14 14" aria-hidden="true"><rect x="1" y="3" width="12" height="8.5" fill="var(--ink-grey)"/><path d="M1.5 3.5 L7 8 L12.5 3.5" fill="none" stroke="#fff" stroke-width="1"/></svg>
        hello@hcestates-example.com
      </li>
      <li>
        <svg class="icon" viewBox="0 0 14 14" aria-hidden="true"><circle cx="7" cy="7" r="6" fill="var(--brand-blue)"/></svg>
        /hcestates
      </li>
      <li>
        <svg class="icon" viewBox="0 0 14 14" aria-hidden="true"><circle cx="7" cy="7" r="6" fill="var(--chat-green)"/></svg>
        /hcestates
      </li>
      <li>
        <svg class="icon" viewBox="0 0 14 14" aria-hidden="true"><g fill="none" stroke="var(--ink-grey)" stroke-width="1.1"><circle cx="7" cy="7" r="6"/><ellipse cx="7" cy="7" rx="2.6" ry="6"/><path d="M1 7 H13"/></g></svg>
        <span>www.<span class="web-accent">hcestates-example</span>.com</span>
      </li>
    </ul>

    <div class="address">
      <svg class="icon" viewBox="0 0 12 16" aria-hidden="true"><path d="M6 0 A6 6 0 0 1 12 6 Q12 9 6 16 Q0 9 0 6 A6 6 0 0 1 6 0Z" fill="var(--ink-grey)"/><circle cx="6" cy="6" r="2.2" fill="#fff"/></svg>
      <div>Opp. Elmwood Market<br>Harbor Jn. Lakeview Road<br>Greenfield, Kerala, India</div>
    </div>
  </section>

</main>
</body>
</html>
```